We are growing our coaching practice and need some help creating collateral

Our organisation is building a coaching practice. It's going well and we want to take it to the next level. To date, we've done our own basic marketing material (attached), but now we want to create something more substantial that captures our approach and gives us confidence and pride when talking to customers. Things to note - we aren't looking for logo design, that's a separate branding discussion in our organisation. We are looking for someone to take our existing content and make it look good - this might be in the form of a flyer or PPT slide deck for example.
The format we are looking for is the offering title - in this case, 'Coaching', a brief description, and then some further detail.
Target Market(s)
Corporate, Healthcare, IT
Colors
Designer to choose colors to be used in the design.
Look and feel
Each slider illustrates characteristics of the customer's brand and the style your logo design should communicate.

```html
<!DOCTYPE html>
<html lang="en">
<head>
<meta charset="utf-8">
<title>MCX Executive Coaching – Flyer</title>
<link href="https://fonts.googleapis.com/css2?family=Open+Sans:wght@300;400;600;700&family=Oswald:wght@500;600&display=swap" rel="stylesheet">
<style>
:root{
  --stage:#2a2523;
  --paper-top:#fbfbfb;
  --paper-bottom:#ececec;
  --ink:#3a3a3a;
  --ink-soft:#4d4d4d;
  --band:#e4603a;
  --accent:#e8662f;
  --amber:#f28c1e;
  --rule:#c9c9c9;
  --white:#ffffff;
}
*{margin:0;padding:0;box-sizing:border-box}
html,body{width:1200px;height:862px;overflow:hidden}
body{background:var(--stage);position:relative;font-family:"Open Sans",Arial,sans-serif;color:var(--ink)}
.page{position:absolute;top:74px;width:628px;height:879px;transform:scale(.8);transform-origin:0 0;
  background:linear-gradient(180deg,var(--paper-top),var(--paper-bottom));overflow:hidden;box-shadow:0 6px 18px rgba(0,0,0,.45)}
.page--back{left:82px}
.page--front{left:614px}
.shapes{position:absolute;inset:0;width:628px;height:879px}
.abs{position:absolute}

.band-text{color:var(--white);font-weight:700;white-space:nowrap;transform-origin:0 0}
.oswald{font-family:"Oswald","Arial Narrow",sans-serif}
.seal{position:absolute;border-radius:50%;background:var(--white);border:5px solid #d6d6d6;
  display:flex;align-items:center;justify-content:center;box-shadow:0 3px 8px rgba(0,0,0,.18)}
.seal__name{font-family:"Open Sans",sans-serif;font-weight:400;color:#555;letter-spacing:1px}

/* back page */
.coach-title{left:32px;top:348px;font-size:31px;font-weight:700;line-height:1.13;color:var(--ink)}
.coach-bio{left:32px;top:440px;width:278px;font-size:9.4px;line-height:14.2px;color:var(--ink-soft);text-align:justify}
.coach-bio p+p{margin-top:7px}
.divider{left:333px;top:372px;width:1px;height:210px;background:var(--rule)}
.quals-title{left:357px;top:370px;font-size:15px;line-height:18px;color:var(--accent)}
.quals{left:355px;top:435px;width:265px;list-style:none;font-size:9.4px;font-weight:600;color:var(--ink-soft)}
.quals li{display:flex;gap:8px;line-height:12.5px;margin-bottom:6px}
.quals svg{flex:0 0 11px;margin-top:1px}
.facilitate{left:32px;top:620px;width:490px;font-size:14.5px;line-height:21px;font-weight:600;color:var(--accent)}

/* front page */
.wordmark{left:40px;top:28px;font-size:31px;font-weight:300;color:#6a6a6a;letter-spacing:2px}
.offer-title{left:28px;top:395px;font-size:39px;font-weight:700;line-height:1.17;color:var(--ink)}
.offer-copy{left:28px;top:504px;width:302px;color:var(--ink-soft);font-size:8.6px;line-height:13.3px;text-align:justify}
.offer-copy .lead{font-size:12px;line-height:16px;margin-bottom:3px;text-align:left}
.offer-copy p+p{margin-top:8px}
.packages{left:355px;top:440px;width:250px;text-align:center;color:var(--ink)}
.packages h2{font-family:"Oswald",sans-serif;font-weight:600;font-size:23px;line-height:24px;color:var(--accent)}
.packages .p1{font-size:12.5px;font-weight:600;margin-top:4px;line-height:20px}
.packages .sessions{font-size:16px;font-weight:700;line-height:20px}
.packages .p2{font-size:12.5px;font-weight:600;line-height:17px}
.packages .price{font-size:12.5px;font-weight:600;color:var(--accent);margin-top:8px;line-height:17px}
.packages .note{font-size:8.5px;line-height:12.5px;color:var(--ink-soft);margin-top:6px}
.cta{left:349px;top:690px;width:245px;text-align:center;color:var(--white)}
.cta .ask{font-size:11px;font-weight:700;line-height:16px}
.cta .contact{font-size:17px;margin-top:10px}
.cta .contact b{font-weight:700}
.cta .call{font-family:"Oswald",sans-serif;font-weight:600;font-size:22px;margin-top:0}
.cta .mail{font-size:11px;font-weight:600;margin-top:4px;letter-spacing:.3px}
.footer-call{left:28px;top:790px;color:var(--white);font-size:22px;font-weight:600}
.footer-web{left:28px;top:824px;color:var(--white);font-size:23.5px;font-weight:700;letter-spacing:.5px}
</style>
</head>
<body>

<section class="page page--back" aria-label="Flyer back: coach profile">
  <svg class="shapes" viewBox="0 0 628 879">
    <defs>
      <linearGradient id="seminar" x1="0" y1="0" x2="1" y2="1">
        <stop offset="0" stop-color="#e9ece9"/><stop offset=".45" stop-color="#a59a8c"/><stop offset="1" stop-color="#3e3a38"/>
      </linearGradient>
      <linearGradient id="desk" x1="0" y1="0" x2="1" y2="0">
        <stop offset="0" stop-color="#5f6c80"/><stop offset=".6" stop-color="#c9c2b6"/><stop offset="1" stop-color="#8a7f70"/>
      </linearGradient>
    </defs>
    <polygon points="0,0 628,0 628,322 0,246" fill="url(#seminar)" role="img" aria-label="Photo of a seminar audience listening to a presenter"/>
    <polygon points="0,246 628,322 628,366 0,290" fill="var(--band)"/>
    <rect x="30" y="668" width="355" height="110" fill="#e6e6e6" role="img" aria-label="Illustration: coaching word with icons for motivation, coach, potential, development, skill, support, knowledge and advice"/>
    <polygon points="0,812 628,762 628,772 0,822" fill="#bdbdbd"/>
    <polygon points="0,822 628,772 628,879 0,879" fill="url(#desk)" role="img" aria-label="Photo of a desk with laptop, mouse and papers"/>
  </svg>

  <div class="abs band-text" style="left:35px;top:262px;font-size:22px;letter-spacing:1.5px;transform:rotate(7deg)">www.meridiancoach.com</div>
  <div class="abs band-text oswald" style="left:425px;top:308px;font-size:21px;transform:rotate(7deg)">Call: 0400 123 456</div>

  <h1 class="abs coach-title">Meet one of our<br>Coaches</h1>
  <div class="abs coach-bio">
    <p>Sam Porter leads the Executive Coaching practice for MCX across Australia and New Zealand.</p>
    <p>He has worked at senior levels in the ACT Public Service, the Australian Public Service and in the private sector. His continuing focus over the past 20 years has been on organisational and people development. As a Masters-qualified and highly experienced executive coach, Sam's passion lies in unlocking human potential. He has coached doctors, nurses, allied health clinicians, statisticians, scientists, educators, IT professionals, Senior managers and Executives in the APS (EL1 – SES), ACT Government (SOGC – Executive bands) and private sector.</p>
  </div>
  <div class="abs divider"></div>
  <h2 class="abs quals-title">Qualifications,<br>Accreditations,<br>Memberships</h2>
  <ul class="abs quals">
    <li><svg width="11" height="11" viewBox="0 0 11 11"><rect x=".5" y=".5" width="10" height="10" fill="none" stroke="var(--accent)"/><path d="M2.5 5.5l2 2 4-5" fill="none" stroke="#4a78b5" stroke-width="1.5"/></svg>Master of Science in Coaching Psychology</li>
    <li><svg width="11" height="11" viewBox="0 0 11 11"><rect x=".5" y=".5" width="10" height="10" fill="none" stroke="var(--accent)"/><path d="M2.5 5.5l2 2 4-5" fill="none" stroke="#4a78b5" stroke-width="1.5"/></svg>Graduate Certificate in Management</li>
    <li><svg width="11" height="11" viewBox="0 0 11 11"><rect x=".5" y=".5" width="10" height="10" fill="none" stroke="var(--accent)"/><path d="M2.5 5.5l2 2 4-5" fill="none" stroke="#4a78b5" stroke-width="1.5"/></svg>Certificate IV in Workplace Assessment &amp; Training</li>
    <li><svg width="11" height="11" viewBox="0 0 11 11"><rect x=".5" y=".5" width="10" height="10" fill="none" stroke="var(--accent)"/><path d="M2.5 5.5l2 2 4-5" fill="none" stroke="#4a78b5" stroke-width="1.5"/></svg>Culture Inventory Accreditation, Peak Synergy</li>
    <li><svg width="11" height="11" viewBox="0 0 11 11"><rect x=".5" y=".5" width="10" height="10" fill="none" stroke="var(--accent)"/><path d="M2.5 5.5l2 2 4-5" fill="none" stroke="#4a78b5" stroke-width="1.5"/></svg>Personality Type Accreditation</li>
    <li><svg width="11" height="11" viewBox="0 0 11 11"><rect x=".5" y=".5" width="10" height="10" fill="none" stroke="var(--accent)"/><path d="M2.5 5.5l2 2 4-5" fill="none" stroke="#4a78b5" stroke-width="1.5"/></svg>Member, Global Coaching Guild (GCG)</li>
    <li><svg width="11" height="11" viewBox="0 0 11 11"><rect x=".5" y=".5" width="10" height="10" fill="none" stroke="var(--accent)"/><path d="M2.5 5.5l2 2 4-5" fill="none" stroke="#4a78b5" stroke-width="1.5"/></svg>Member, Coastal University Coaching &amp;<br>Mentoring Alumni Association</li>
  </ul>
  <p class="abs facilitate">When Sam is not coaching, he is facilitating workshops and consulting to enable teams and organisations to make effective transformations.</p>
  <div class="seal" style="left:455px;top:655px;width:150px;height:150px"><span class="seal__name" style="font-size:38px">MCX</span></div>
</section>

<section class="page page--front" aria-label="Flyer front: executive coaching offer">
  <svg class="shapes" viewBox="0 0 628 879">
    <defs>
      <linearGradient id="bridge" x1="0" y1="0" x2="0" y2="1">
        <stop offset="0" stop-color="#f4f5f4"/><stop offset=".25" stop-color="#5f7a5a"/><stop offset=".6" stop-color="#7b5a3a"/><stop offset="1" stop-color="#8fa0a2"/>
      </linearGradient>
    </defs>
    <polygon points="0,55 628,55 628,388 0,328" fill="url(#bridge)" role="img" aria-label="Photo of a wooden truss bridge crossing a river in front of a forest"/>
    <polygon points="0,328 628,388 628,430 0,370" fill="var(--band)"/>
    <polygon points="0,760 330,780 330,790 0,770" fill="#b8b8b8"/>
    <polygon points="0,770 330,790 330,879 0,879" fill="var(--band)"/>
    <circle cx="480" cy="905" r="234" fill="var(--white)"/>
    <circle cx="480" cy="905" r="226" fill="var(--amber)"/>
  </svg>

  <div class="abs wordmark">meridian coaching</div>
  <div class="abs band-text" style="left:32px;top:336px;font-size:17px;letter-spacing:.3px;transform:rotate(5.5deg)">Focusing on leadership, teams, technology and enterprise-wide</div>

  <h1 class="abs offer-title">MCX Executive<br>Coaching</h1>
  <div class="abs offer-copy">
    <p class="lead">We believe great coaching is a bridge:</p>
    <p style="margin-top:0">one that enables you to see more clearly and cross the unexpected chasms; one that supports and challenges your thinking and actions to progress your significant goals.</p>
    <p>We build a creative and confidential partnership with you, one that is grounded in the science of leadership, change and coaching psychology so that practical results are an expectation and not left to chance.</p>
    <p>Our coaches are highly attuned to the human systems within which you work and live, since understanding those interconnected forces is vital to unlock movement. We build on your existing strengths and seek sustainable shifts, ones that create ripple effects of positive change.</p>
    <p>Leaders everywhere face unprecedented change, pressure, ambiguity, culture and accountability dilemmas. And yet every leader also has a different story, different terrain to navigate and different aspirations. This is where executive coaching with MCX can create extraordinary results.</p>
  </div>

  <div class="abs packages">
    <h2>OUR COACHING<br>PACKAGES</h2>
    <p class="p1">typically consist of blocks of</p>
    <p class="sessions">7 Hourly Sessions,</p>
    <p class="p2">conducted fortnightly<br>(with flexibility to customise).</p>
    <p class="price">For EL2 leaders, the investment in a<br>block of 7 sessions is $3400 + GST.</p>
    <p class="note">This includes significant preparation and conceptualisation time before and after sessions by your coach to ensure you achieve maximum value.</p>
  </div>

  <div class="abs cta">
    <p class="ask">Why not explore the<br>possibilities executive coaching<br>offers through a no obligation initial<br>session, ensuring the approach and the<br>coach is a good fit for you?</p>
    <p class="contact">Contact <b>Sam Porter</b></p>
    <p class="call">Call: 0400 123 456</p>
    <p class="mail">sam.porter@meridiancoach.com</p>
  </div>

  <div class="abs footer-call oswald">Call us: 0400 123 456</div>
  <div class="abs footer-web">meridiancoach.com</div>
  <div class="seal" style="left:268px;top:750px;width:100px;height:100px"><span class="seal__name" style="font-size:25px">MCX</span></div>
</section>

</body>
</html>
```